Digital Price Menus for Detail Shop

I am looking to have digital menus for my detail shop. I have 3 55-inch TVs (see pictures) on how they are situated on the wall for my front desk area. They will be vertical, not horizontal.

Color pallet I am looking for is black and gold, with some accent colors if applicable. I would like black background with some sort of design in it in such a way it looks faint or ghosted in the background ... i.e., honeycomb, splatter, etc. A boarder is optional.

Needs to be designed well, organized well and easy to read for customers walking in.

the each document is for each TV, Interior, Exterior and Ceramic Coatings

Company logo files included. would like my logos on them as well

Target Market(s)

Customers walking in to my shop, easy to read and understand

Industry/Entity Type

Car wash, Detailing

Colors

Designer to choose only greyscale colors for use in the design.

Requirements
Nice to have
• Professional Look
Should not have
• tacky look

```html
<!DOCTYPE html>
<html lang="en">
<head>
<meta charset="utf-8">
<title>Ceramic Coatings Menu</title>
<link rel="stylesheet" href="https://fonts.googleapis.com/css2?family=Barlow+Condensed:wght@600;700&family=Open+Sans:ital,wght@0,400;0,600;0,700;1,600;1,700&display=swap">
<style>
  :root {
    --stage: #f3f3f1;
    --ink: #0d0d0f;
    --panel-dark: #1a1b20;
    --panel-deep: #0b0c0f;
    --white: #ffffff;
    --rule: #8a8a8a;
    --gold-dark: #b07d17;
    --gold-mid: #e0b53a;
    --gold-light: #fbe79a;
  }
  * { box-sizing: border-box; margin: 0; padding: 0; }
  html, body { width: 979px; height: 1200px; overflow: hidden; background: var(--stage); }
  body { position: relative; font-family: "Open Sans", sans-serif; color: var(--white); }

  .menu {
    position: absolute; left: 217px; top: 116px; width: 545px; height: 967px;
    background: radial-gradient(ellipse at 50% 40%, var(--panel-dark), var(--panel-deep));
    overflow: hidden;
  }
  .menu-texture {
    position: absolute; inset: 0;
    background: radial-gradient(ellipse at 50% 50%, rgba(255,255,255,0.04), rgba(255,255,255,0) 70%);
  }
  .gold-band {
    position: absolute; left: 0; width: 100%;
    background: linear-gradient(90deg, var(--gold-dark) 0%, var(--gold-mid) 22%, var(--gold-light) 50%, var(--gold-mid) 78%, var(--gold-dark) 100%);
    color: var(--ink);
  }
  .header-band { top: 0; height: 160px; }
  .glass-band { top: 579px; height: 130px; text-align: center; }
  .footer-band { top: 945px; height: 22px; }

  .display { font-family: "Barlow Condensed", sans-serif; font-weight: 600; line-height: 1; }

  .menu-title { position: absolute; left: 21px; top: 22px; font-size: 55px; letter-spacing: 0.2px; }
  .menu-intro {
    position: absolute; left: 21px; top: 78px; width: 364px;
    font-size: 9.9px; line-height: 14.9px; text-align: justify;
  }
  .brand {
    position: absolute; left: 392px; top: 54px; width: 140px; text-align: center;
  }
  .brand-mark { display: block; width: 12px; height: 12px; background: var(--ink); margin: 0 auto 8px; border-radius: 50%; }
  .brand-name { font-family: "Barlow Condensed", sans-serif; font-weight: 600; font-size: 25px; line-height: 1.02; }
  .brand-tag { font-family: "Barlow Condensed", sans-serif; font-weight: 600; font-size: 25px; line-height: 1.02; }

  .lead {
    position: absolute; left: 21px; top: 173px; width: 490px;
    font-size: 12.8px; font-style: italic; font-weight: 700; line-height: 19.5px;
  }

  .service { position: absolute; left: 21px; width: 502px; }
  .service-row { display: flex; align-items: flex-end; }
  .service-name { font-size: 40px; white-space: nowrap; }
  .leader { flex: 1; border-bottom: 1px solid var(--rule); margin: 0 4px 3px 4px; }
  .starting {
    background: var(--white); color: var(--ink); font-size: 9.5px; font-weight: 700;
    padding: 2px 6px; margin: 0 8px 4px 0; white-space: nowrap; letter-spacing: 0.3px;
  }
  .price { font-size: 40px; }
  .service-desc { font-size: 13.8px; line-height: 20px; margin-top: 3px; }
  .service-desc strong { font-size: 15.5px; font-weight: 700; }

  .svc-1 { top: 242px; }
  .svc-3 { top: 335px; }
  .svc-5 { top: 408px; }
  .svc-wheel-face { top: 739px; }
  .svc-wheel-off { top: 837px; }
  .svc-wheel-face .service-desc, .svc-wheel-off .service-desc { line-height: 19px; }

  .note {
    position: absolute; left: 21px; top: 505px; width: 500px;
    font-size: 23px; font-style: italic; font-weight: 600; line-height: 29px;
  }

  .glass-title { font-size: 57px; margin-top: 18px; letter-spacing: 0.2px; }
  .glass-price { display: flex; justify-content: center; align-items: baseline; gap: 16px; margin-top: 4px; }
  .glass-price .label { font-family: "Open Sans", sans-serif; font-weight: 700; font-size: 25px; letter-spacing: 1px; }
  .glass-price .amount { font-size: 44px; }
</style>
</head>
<body>
  <main class="menu">
    <div class="menu-texture" role="img" aria-label="Faint honeycomb texture across the dark background"></div>

    <header class="gold-band header-band">
      <h1 class="display menu-title">CERAMIC COATINGS</h1>
      <p class="menu-intro">All ceramic coating packages start with a Paint enhancement package. The 1 step polish will improve the appearance of blemishes, light marring and scratching 50-70%. On new cars it will reach up to 95%+ improvement. A full paint correction can be added for an additional cost. Day of pick up, a Sealant is applied to all coated surfaces to help with the curing process.</p>
      <div class="brand">
        <span class="brand-mark"></span>
        <div class="brand-name">Northline</div>
        <div class="brand-tag">Detail</div>
      </div>
    </header>

    <p class="lead">Not every customer has the same goals when it comes to coatings so we have developed 3 different levels to choose from depending on your wants and needs and budget.</p>

    <section class="service svc-1">
      <div class="service-row">
        <h2 class="display service-name">1 YEAR COATING</h2><span class="leader"></span>
        <span class="starting">STARTING AT</span><span class="display price">$500</span>
      </div>
      <p class="service-desc">Applied to all painted surfaces, provides up to <strong>12months</strong> of durability.<br>Add asecond layer for <strong>$600</strong> more for <strong>18-24 months</strong> of protection.</p>
    </section>

    <section class="service svc-3">
      <div class="service-row">
        <h2 class="display service-name">3 YEAR COATING</h2><span class="leader"></span>
        <span class="starting">STARTING AT</span><span class="display price">$800</span>
      </div>
      <p class="service-desc">Applied to all painted surfaces, provides up to <strong>36 months</strong> of durability</p>
    </section>

    <section class="service svc-5">
      <div class="service-row">
        <h2 class="display service-name">5 YEAR COATING</h2><span class="leader"></span>
        <span class="starting">STARTING AT</span><span class="display price">$1000</span>
      </div>
      <p class="service-desc">Warrantied paint coating, applied to all painted surfaces, provides up to<br><strong>60 months</strong> of durability</p>
    </section>

    <p class="note">• Durability is directly related to the proper maintenance of the coatings.</p>

    <section class="gold-band glass-band">
      <h2 class="display glass-title">GLASS CERAMIC COATING</h2>
      <div class="glass-price"><span class="label">STARTING AT</span><span class="display amount">$1000</span></div>
    </section>

    <section class="service svc-wheel-face">
      <div class="service-row">
        <h2 class="display service-name">WHEEL FACE COATING</h2><span class="leader"></span>
        <span class="starting">STARTING AT</span><span class="display price">$1000</span>
      </div>
      <p class="service-desc">Warrantied paint coating, applied to all painted surfaces, provides up to<br><strong>60 months</strong> of durability</p>
    </section>

    <section class="service svc-wheel-off">
      <div class="service-row">
        <h2 class="display service-name">WHEEL OFF COATING</h2><span class="leader"></span>
        <span class="starting">STARTING AT</span><span class="display price">$250</span>
      </div>
      <p class="service-desc">Wheel coating package + durable industrial coating on barrels of wheels<br>and if applicable, calipers and suspension components.</p>
    </section>

    <footer class="gold-band footer-band"></footer>
  </main>
</body>
</html>
```